Design for Magento Sports ecommerce

Looking for a design (the PSD's only) for a web shop selling sports equipment.
We are using Magento but feel free to change any of the standard features/elements in Magento.
We are hoping to see something different and creative. Unlike the usual ecommerce designs from LayoutHarbor etc.

The main categories will be: Running (shoes, clothes etc), football (soccer), Handball, Cycling(equipment only), Fitness, Tennis and Swimming.
Lots of subcategories so easy navigation, like a dropdown, megamenu, might be an obvious choice.

The design should at least include suggestions for: Home Page, Product list, Product view and a CMS page (like About Us).
Updates

Hi everybody

Thanks for all the proposals on the project.
There're some really great ones and I appreciate the time and effort you all put into this.
I'm busy walking through each one and will get back as soon as possible.

Tomas

Target Market(s)

Male & Females between 18-60. anyone doing sports in above categories.

Industry/Entity Type

Fitness

Requirements
Must have
• Filter/Layered Navigation is important. We use Kelvora. See here:
http://www.kelvora-apps.com/demo/seo-layered-navigation-plus/

Manufacturers logo on Product view page.

Related products / Upselling on Product view page.
Nice to have
• Product labels/stickers for marking New products, Special offer etc on Product List and Product View.

Icons instead of text links for Cart, My Account, sorting etc.

Responsive design that can make use of widescreen monitors as well as tablets.

The use of "handwriting" or handwritten icons, like here on pixelforum(sorry), looks awesome. :-)
Should not have
• you can disregard the following Magento features:
Wish list
Email a friend
Reviews

```html
<!DOCTYPE html>
<html lang="en">
<head>
<meta charset="utf-8">
<title>Stridehaus – Sports Gear Shop</title>
<link href="https://fonts.googleapis.com/css2?family=Arimo:wght@400;700&family=Shadows+Into+Light&family=Oswald:wght@500&display=swap" rel="stylesheet">
<style>
:root{
  --blue:#1b6fc4;
  --blue-light:#8ec2ec;
  --blue-pale:#cfe4f7;
  --red:#d3202a;
  --ink:#222;
  --muted:#9a9a9a;
  --panel:#ececec;
  --footer:#d2d2d2;
  --white:#fff;
  --line:#c9c9c9;
}
*{box-sizing:border-box;margin:0;padding:0}
html,body{width:1200px;height:2535px;overflow:hidden;background:var(--white)}
body{position:relative;font-family:'Arimo',Arial,sans-serif;color:var(--ink)}
.abs{position:absolute}
.hand{font-family:'Shadows Into Light',cursive}

/* header */
.site-header{left:0;top:0;width:1200px;height:116px;background:var(--white)}
.brand-mark{left:140px;top:22px;display:flex;align-items:center;gap:12px}
.brand-mark .name{font-family:'Arimo',sans-serif;font-weight:700;font-size:52px;color:var(--ink);letter-spacing:-1px}
.brand-mark .dot{width:40px;height:40px;background:var(--blue)}
.tagline{left:160px;top:90px;font-size:10px;font-weight:700;color:var(--blue);letter-spacing:1px}
.search{left:778px;top:28px;width:183px;height:20px;border-radius:10px;background:linear-gradient(#e9e9e9,#cfcfcf)}
.search svg{position:absolute;right:8px;top:3px}
.login-link{left:1008px;top:32px;font-size:13px;font-weight:700;color:var(--red)}
.cart{left:1005px;top:68px;width:75px;text-align:right;font-size:10px;color:#555;line-height:12px}
.cart svg{display:block;margin:0 0 2px 38px}

.main-nav{left:466px;top:92px;display:flex;gap:8px}
.nav-pill{display:flex;align-items:center;height:28px;padding:0 10px 0 4px;border:2px solid #444;border-radius:14px;background:var(--white);font-size:12px;font-weight:700;color:var(--ink)}
.nav-pill::before{content:"";width:10px;height:10px;border-radius:50%;border:2px solid #444;margin-right:5px}
.nav-pill.active{border-color:var(--blue)}
.nav-pill.sale{background:var(--red);color:var(--white);border-color:var(--red)}
.nav-pill.sale::before{border-color:var(--white)}

/* hero */
.hero{left:0;top:116px;width:1200px;height:518px;background:linear-gradient(100deg,#7b4a2a 0%,#eae4da 18%,#f5f3ef 35%,#d9d0c2 55%,#a8c4dd 75%,#1f5fa8 100%)}
.nav-strip{left:437px;top:140px;width:763px;height:5px;background:var(--blue)}

.mega-menu{left:437px;top:145px;width:624px;height:362px;background:var(--white);box-shadow:0 4px 10px rgba(0,0,0,.25);padding:14px 10px;display:flex;gap:0}
.mega-col{width:154px;font-size:10.5px;line-height:17.5px;color:#333}
.mega-col h4{font-size:11px;font-weight:700;border-bottom:1px solid var(--line);margin-bottom:3px;padding-bottom:2px}
.mega-col h4.gap{margin-top:8px}

.login-box{left:960px;top:476px;width:190px;height:158px;background:var(--white);border:3px solid var(--line);border-bottom:none;border-radius:10px 10px 0 0;padding:10px 12px;font-size:10px}
.login-box h3{font-size:13px;color:var(--red);text-align:right;margin-bottom:18px}
.login-row{display:flex;justify-content:space-between;align-items:center;margin-bottom:26px}
.login-row span{width:92px;height:18px;border:1px solid var(--line);background:#f6f6f6}

/* featured */
.featured{left:0;top:634px;width:1200px;height:750px;background:var(--panel);border-radius:0 0 30px 30px}
.section-title{display:flex;align-items:center;justify-content:center;width:290px;height:56px;position:absolute}
.section-title svg{position:absolute;inset:0}
.section-title span{position:relative;font-family:'Oswald',sans-serif;font-weight:500;font-size:20px;color:var(--red);letter-spacing:.5px}

.sport-card{position:absolute;width:286px}
.sport-card .tab{position:relative;width:160px;height:42px;background:var(--white);border-radius:4px 4px 0 0;padding:6px 14px;font-size:24px;color:var(--blue)}
.sport-card .tab::after{content:"";position:absolute;right:-22px;top:0;border-left:22px solid var(--white);border-top:42px solid transparent}
.sport-card .frame{background:var(--white);padding:6px 6px 4px;box-shadow:0 2px 4px rgba(0,0,0,.12)}
.sport-card .photo{height:164px}
.sport-card .link{font-size:10.5px;color:var(--blue);text-align:right;padding-top:6px;letter-spacing:.2px}
.sport-card p{font-size:10px;color:var(--muted);line-height:12px;padding:10px 8px 0}

/* about */
.about-band{left:0;top:1426px;width:1200px;height:250px;background:var(--blue)}
.about-label{left:140px;top:1452px;width:185px;height:180px;background:var(--white);border-left:10px solid var(--blue-light)}
.about-label .sq{position:absolute;left:16px;top:18px;width:50px;height:50px;background:var(--blue)}
.about-label h2{position:absolute;left:14px;bottom:16px;font-size:24px;color:var(--blue);border-bottom:3px solid var(--blue);padding-bottom:2px}
.about-text{left:325px;top:1452px;width:474px;height:180px;background:var(--blue-light);padding:16px 20px;color:var(--white);font-size:12.5px;line-height:16px;text-align:justify}
.about-text .more{position:absolute;right:20px;bottom:12px;font-size:12px}
.about-text::after{content:"";position:absolute;left:360px;bottom:-22px;border-top:22px solid var(--blue-light);border-right:22px solid transparent}
.follow{left:803px;top:1452px;width:242px;height:180px;background:var(--blue-light);border:3px solid var(--white)}
.follow .label{position:absolute;left:-8px;top:74px;transform:rotate(-90deg);font-size:26px;color:var(--white)}
.follow-grid{position:absolute;left:52px;top:20px;display:grid;grid-template-columns:1fr 1fr;gap:22px 10px}
.social-item{display:flex;align-items:center;gap:5px;font-size:11px;color:var(--white);font-weight:700}
.social-item i{width:16px;height:16px;border-radius:50%;border:2px solid var(--white)}

/* products */
.products{left:0;top:1754px;width:1200px;height:232px;background:#f4f4f4;border-top:1px solid var(--line);border-bottom:1px solid var(--line)}
.product-row{left:131px;top:1754px;width:921px;height:232px;display:flex}
.product{position:relative;flex:1;background:var(--white);border-right:1px solid var(--line);padding:12px 8px}
.product h3{font-size:13.5px;font-weight:400;color:#333;text-align:center}
.product .shot{width:130px;height:130px;margin:14px auto 0}
.product .maker{position:absolute;left:10px;bottom:14px;font-size:12px;font-weight:700;color:var(--ink)}
.product .price{position:absolute;right:8px;bottom:10px;height:26px;padding:0 8px;border-radius:13px;background:var(--red);color:var(--white);font-size:10px;font-weight:700;line-height:26px}
.product .badge-new{position:absolute;right:12px;top:46px;width:36px;height:36px;border-radius:50%;background:var(--red);color:var(--white);font-size:10px;font-weight:700;text-align:center;line-height:36px}
.slide-arrow{width:40px;height:40px;background:#8c8c8c;display:flex;align-items:center;justify-content:center}

/* brands */
.brand-row{left:140px;top:2076px;width:920px;display:flex;align-items:center;justify-content:space-between}
.brand-row .logo-name{font-size:17px;font-weight:700;color:#777}
.brand-rule{left:0;top:2138px;width:1200px;height:4px;background:var(--blue)}

/* footer */
.site-footer{left:0;top:2142px;width:1200px;height:330px;background:var(--footer)}
.foot-panel{position:absolute;top:2200px;width:208px;height:240px;background:var(--white);border:4px solid #9a9a9a;border-radius:20px;padding:36px 16px 0}
.foot-panel .cap{position:absolute;left:50%;top:-22px;transform:translateX(-50%);width:96px;height:34px;background:linear-gradient(#f3f3f3,#cfcfcf);border:3px solid #9a9a9a;border-radius:8px;font-size:17px;color:#666;text-align:center;line-height:26px}
.foot-list{list-style:none;font-size:16px;color:var(--blue);line-height:28px}
.foot-list li::before{content:"•";margin-right:6px;color:var(--blue)}
.pay-grid{display:grid;grid-template-columns:1fr 1fr;gap:14px 10px;margin-top:6px}
.pay-badge{height:44px;border:2px solid var(--blue);border-radius:50%;font-size:10.5px;font-weight:700;color:var(--blue);display:flex;align-items:center;justify-content:center;text-align:center}
.soc-grid{display:grid;grid-template-columns:1fr 1fr;gap:30px 8px;margin-top:18px}
.soc-grid .social-item{color:var(--blue);font-size:11px}
.soc-grid .social-item i{border-color:var(--blue)}
.legal{left:0;top:2472px;width:1200px;height:63px;background:var(--blue);color:var(--white);font-size:13px;text-align:center;line-height:63px}
</style>
</head>
<body>

<header class="abs site-header">
  <div class="abs brand-mark"><span class="name">Stridehaus</span><span class="dot"></span></div>
  <div class="abs tagline">NUMBER 1 IN SPORT'S</div>
  <div class="abs search"><svg width="14" height="14" viewBox="0 0 14 14"><circle cx="6" cy="6" r="4" fill="none" stroke="#555" stroke-width="1.6"/><line x1="9" y1="9" x2="13" y2="13" stroke="#555" stroke-width="1.6"/></svg></div>
  <div class="abs login-link">LOG IN</div>
  <div class="abs cart">
    <svg width="36" height="30" viewBox="0 0 36 30"><path d="M2 4h6l4 16h18l4-12H10" fill="none" stroke="#555" stroke-width="2"/><circle cx="14" cy="25" r="2.5" fill="#555"/><circle cx="27" cy="25" r="2.5" fill="#555"/></svg>
    Total: 0.00<br>Items: 0
  </div>
</header>

<div class="abs hero" role="img" aria-label="Hero photograph: clipboard with handwritten note reading Your one-stop online sports gear shop, surrounded by a rugby ball, football, boxing glove, baseball glove and tennis balls"></div>
<div class="abs nav-strip"></div>

<nav class="abs main-nav">
  <span class="nav-pill">MENS</span>
  <span class="nav-pill">LADIES</span>
  <span class="nav-pill active">JUNIOR</span>
  <span class="nav-pill">SPORTS</span>
  <span class="nav-pill">BRANDS</span>
  <span class="nav-pill">NEWS</span>
  <span class="nav-pill sale">SALE</span>
</nav>

<div class="abs mega-menu">
  <div class="mega-col">
    <h4>Footwear</h4>
    Astro Trainers<br>Basketball Shoes<br>Boots<br>Canvas Shoes<br>Fitness Training<br>Football Boots<br>Golf Shoes<br>Hi Tops<br>Indoor and Court Trainers<br>Indoor Football Trainers<br>Rebound Classic Trainers<br>Running Shoes<br>Sandals and Flip Flops<br>Shoes<br>Skate Shoes<br>Trainers<br>Walking Boots<br>Wellies
  </div>
  <div class="mega-col">
    <h4>Clothing</h4>
    Base Layer<br>Bikinis and Tankinis<br>Chinos<br>Combats<br>Fitness Clothing<br>Fleeces<br>Gilets<br>Hoodies<br>Jackets and Coats<br>Jeans<br>Knitwear<br>Plus Size<br>Polo Shirts<br>Shirts<br>Shorts<br>Skirts and Dresses<br>Socks
  </div>
  <div class="mega-col">
    <h4>&nbsp;</h4>
    Sweat Pants<br>Three Quarter Pants<br>Tights and Leggings<br>Tracksuit Bottoms<br>Tracksuits<br>T-Shirts<br>Underwear<br>Vests<br>Waterproofs<br>Zip Tops
    <h4 class="gap">Fashion Outlet</h4>
    Tops and T-Shirts<br>Hoodies and Jackets<br>Pants and Trousers<br>New Discounts
  </div>
  <div class="mega-col">
    <h4>Accessories</h4>
    Belts<br>Caps<br>Gloves, Hats and Scarves<br>Hair Accessories<br>Jewellery<br>Slippers<br>Sunglasses<br>Watches
    <h4 class="gap">Clearance</h4>
    Jackets<br>Bottoms<br>Tops<br>Footwear
  </div>
</div>

<div class="abs login-box">
  <h3>LOG IN</h3>
  <div class="login-row">user name <span></span></div>
  <div class="login-row">password <span></span></div>
</div>

<section class="abs featured"></section>
<div class="section-title" style="left:138px;top:662px">
  <svg viewBox="0 0 290 56"><ellipse cx="145" cy="28" rx="140" ry="22" fill="none" stroke="var(--red)" stroke-width="2"/><ellipse cx="148" cy="27" rx="134" ry="18" fill="none" stroke="var(--red)" stroke-width="1"/></svg>
  <span>FEATURED SPORTS</span>
</div>

<article class="sport-card" style="left:158px;top:744px">
  <div class="tab hand">Tennis</div>
  <div class="frame"><div class="photo" role="img" aria-label="Tennis player serving against a bright blue sky" style="background:linear-gradient(160deg,#eef6fd,#5aa2e0 60%,#2a6db8)"></div><div class="link">VIEW OUR TENNIS GEAR PORFOLIO ▶</div></div>
  <p>Lorem ipsum dolor sit amet, has commodo officiis cu, amet offendit ius et, ne has putant option voluptua. Id eros commodo</p>
</article>
<article class="sport-card" style="left:458px;top:744px">
  <div class="tab hand">Football</div>
  <div class="frame"><div class="photo" role="img" aria-label="Two footballers competing for the ball under stadium lights" style="background:radial-gradient(circle at 50% 30%,#b9c2c9,#3c4650 60%,#15191d)"></div><div class="link">VIEW OUR FOOTBALL GEAR PORFOLIO ▶</div></div>
  <p>Lorem ipsum dolor sit amet, has commodo officiis cu, amet offendit ius et, ne has putant option voluptua. Id eros commodo</p>
</article>
<article class="sport-card" style="left:754px;top:744px">
  <div class="tab hand">Handball</div>
  <div class="frame"><div class="photo" role="img" aria-label="Handball player about to throw the ball on a dark background" style="background:linear-gradient(90deg,#111,#2a2a2a 45%,#d9dde2 55%,#111 80%)"></div><div class="link">VIEW OUR HANDBALL GEAR PORFOLIO ▶</div></div>
  <p>Lorem ipsum dolor sit amet, has commodo officiis cu, amet offendit ius et, ne has putant option voluptua. Id eros commodo</p>
</article>

<article class="sport-card" style="left:158px;top:1063px">
  <div class="tab hand">Swimming</div>
  <div class="frame"><div class="photo" role="img" aria-label="Swimmer mid-stroke with water splashing on black" style="background:radial-gradient(circle at 50% 50%,#6fa2c2,#1b2e3c 55%,#050708)"></div><div class="link">VIEW OUR SWIMMING GEAR PORFOLIO ▶</div></div>
  <p>Lorem ipsum dolor sit amet, has commodo officiis cu, amet offendit ius et, ne has putant option voluptua. Id eros commodo</p>
</article>
<article class="sport-card" style="left:458px;top:1063px">
  <div class="tab hand">Cycling</div>
  <div class="frame"><div class="photo" role="img" aria-label="Road cyclist riding through green countryside" style="background:linear-gradient(180deg,#5f7f45,#344a2a 55%,#8a8f84)"></div><div class="link">VIEW OUR FOOTBALL GEAR PORFOLIO ▶</div></div>
  <p>Lorem ipsum dolor sit amet, has commodo officiis cu, amet offendit ius et, ne has putant option voluptua. Id eros commodo</p>
</article>
<article class="sport-card" style="left:754px;top:1063px">
  <div class="tab hand">Running</div>
  <div class="frame"><div class="photo" role="img" aria-label="Runner leaping in front of a city skyline" style="background:linear-gradient(180deg,#d7d9dc,#8d949b 60%,#3f454b)"></div><div class="link">VIEW OUR HANDBALL GEAR PORFOLIO ▶</div></div>
  <p>Lorem ipsum dolor sit amet, has commodo officiis cu, amet offendit ius et, ne has putant option voluptua. Id eros commodo</p>
</article>

<section class="abs about-band"></section>
<div class="abs about-label"><span class="sq"></span><h2>ABOUT US</h2></div>
<div class="abs about-text">
  Lorem ipsum dolor sit amet, consectetuer adipiscing elit, sed diam nonummy nibh euismod tincidunt ut laoreet dolore magna aliquam erat volutpat. Ut wisi enim ad minim veniam, quis nostrud exerci tation ullamcorper suscipit lobortis nisl ut aliquip ex ea commodo consequat. Duis autem vel eum iriure dolor in hendrerit in vulputate velit esse molestie consequat, vel illum dolore eu feugiat nulla facilisis at vero eros et accumsan
  <span class="more">READ MORE &gt;</span>
</div>
<div class="abs follow">
  <span class="label hand">follow us</span>
  <div class="follow-grid">
    <span class="social-item"><i></i>Friendsy</span>
    <span class="social-item"><i></i>Chirper</span>
    <span class="social-item"><i></i>Workwise</span>
    <span class="social-item"><i></i>Pinboardly</span>
  </div>
</div>

<div class="section-title" style="left:138px;top:1683px">
  <svg viewBox="0 0 290 56"><ellipse cx="145" cy="28" rx="140" ry="22" fill="none" stroke="var(--red)" stroke-width="2"/><ellipse cx="148" cy="27" rx="134" ry="18" fill="none" stroke="var(--red)" stroke-width="1"/></svg>
  <span>POPULAR PRODUCTS</span>
</div>

<section class="abs products"></section>
<div class="abs slide-arrow" style="left:0;top:1850px"><svg width="14" height="18"><path d="M11 2L3 9l8 7" fill="none" stroke="#fff" stroke-width="3"/></svg></div>
<div class="abs slide-arrow" style="left:1160px;top:1850px"><svg width="14" height="18"><path d="M3 2l8 7-8 7" fill="none" stroke="#fff" stroke-width="3"/></svg></div>
<div class="abs product-row">
  <div class="product"><h3>PRODUCT NAME/DESC</h3><div class="shot" role="img" aria-label="White sports t-shirt" style="background:radial-gradient(#fff,#e2e2e2)"></div><span class="maker">Tristra</span><span class="price">ONLY 0000.00</span></div>
  <div class="product"><h3>PRODUCT NAME/DESC</h3><div class="shot" role="img" aria-label="White sports sock" style="background:radial-gradient(#fafafa,#d6d6d6)"></div><span class="badge-new">NEW</span><span class="maker">Donvale</span><span class="price">ONLY 0000.00</span></div>
  <div class="product"><h3>PRODUCT NAME/DESC</h3><div class="shot" role="img" aria-label="Grey and blue running shoe" style="background:radial-gradient(#c9ccd2,#7f8a99)"></div><span class="maker">Swoopa</span><span class="price">ONLY 0000.00</span></div>
  <div class="product"><h3>PRODUCT NAME/DESC</h3><div class="shot" role="img" aria-label="Black training shorts" style="background:radial-gradient(#555,#1c1c1c)"></div><span class="maker">Tristra</span><span class="price">ONLY 0000.00</span></div>
  <div class="product" style="border-right:none"><h3>PRODUCT NAME/DESC</h3><div class="shot" role="img" aria-label="Orange football shirt" style="background:radial-gradient(#ff7a4a,#e24a1c)"></div><span class="maker">Swoopa</span><span class="price">ONLY 0000.00</span></div>
</div>

<div class="section-title" style="left:138px;top:2005px">
  <svg viewBox="0 0 290 56"><ellipse cx="145" cy="28" rx="140" ry="22" fill="none" stroke="var(--red)" stroke-width="2"/><ellipse cx="148" cy="27" rx="134" ry="18" fill="none" stroke="var(--red)" stroke-width="1"/></svg>
  <span>OUR BRANDS</span>
</div>
<div class="abs brand-row">
  <svg width="14" height="20"><path d="M11 2L3 10l8 8" fill="none" stroke="var(--red)" stroke-width="3"/></svg>
  <span class="logo-name">Swoopa</span>
  <span class="logo-name">Tristra</span>
  <span class="logo-name">Dimondo</span>
  <span class="logo-name">Pantera</span>
  <span class="logo-name">Dunmere</span>
  <span class="logo-name">Lonmark</span>
  <span class="logo-name">Karrow</span>
  <span class="logo-name">Slazebury</span>
  <svg width="14" height="20"><path d="M3 2l8 8-8 8" fill="none" stroke="var(--red)" stroke-width="3"/></svg>
</div>
<div class="abs brand-rule"></div>

<footer class="abs site-footer"></footer>
<div class="foot-panel" style="left:144px">
  <span class="cap hand">shopping</span>
  <ul class="foot-list hand"><li>My Account</li><li>Delivery</li><li>Payment Methods</li><li>Size Guidelines</li><li>Order History</li><li>Order Tracking</li><li>Returns</li></ul>
</div>
<div class="foot-panel" style="left:380px">
  <span class="cap hand">help</span>
  <ul class="foot-list hand"><li>FAQs</li><li>Contact us</li><li>About us</li><li>Security / Privacy</li><li>Careers</li><li>Cookies</li><li>Terms / Conditions</li></ul>
</div>
<div class="foot-panel" style="left:613px">
  <span class="cap hand">payment</span>
  <div class="pay-grid">
    <span class="pay-badge">Vantix</span><span class="pay-badge">Mercacard</span>
    <span class="pay-badge">Orbipay</span><span class="pay-badge">PayWisp</span>
    <span class="pay-badge">Amerion Xpress</span><span class="pay-badge">Solvo</span>
  </div>
</div>
<div class="foot-panel" style="left:849px">
  <span class="cap hand">social media</span>
  <div class="soc-grid">
    <span class="social-item"><i></i>Friendsy</span><span class="social-item"><i></i>Chirper</span>
    <span class="social-item"><i></i>Workwise</span><span class="social-item"><i></i>Pinboardly</span>
  </div>
</div>
<div class="abs legal">© 2013 &nbsp;|&nbsp; Sitemap &nbsp;|&nbsp; Legal Disclaimer</div>

</body>
</html>
```